Tomas Villacreces Business Cards

Hello everyone,

I need business cards designed to the following specs:

3.5"x2" with .25" bleed all around for printing
Square corners only

Front:

(Use picture attached)
Tomas Villacreces
Real Estate Professional

305-847-2396
brightkoda@ nestmail.com
(no Space)
Instagram logo @brightkoda
Facebook logo Tomas Villacreces
LinkedIn Tomas Villacreces
4829 NW 127th St STE 200
Palm Hollow, FL 33092

Back:

Harborview logo

```html
<!DOCTYPE html>
<html lang="en">
<head>
<meta charset="utf-8">
<title>Harborview – Tomas Villacreces Business Cards</title>
<link rel="stylesheet" href="https://fonts.googleapis.com/css2?family=Montserrat:wght@400;600;700&display=swap">
<style>
  :root {
    --bg: #ece8e2;
    --card-dark: #0b0b0c;
    --card-mid: #1c1c1e;
    --ink-light: #f4f4f4;
    --ink-soft: #d8d8d8;
    --accent-red: #e0262f;
    --photo-light: #f7f7f7;
    --photo-mid: #c9c6c2;
    --icon-ig: #d8407a;
    --icon-fb: #3b5ba8;
    --icon-in: #2a7bbf;
  }
  * { margin: 0; padding: 0; box-sizing: border-box; }
  html, body {
    width: 1200px; height: 885px; overflow: hidden;
    background: var(--bg);
    font-family: "Montserrat", Arial, sans-serif;
  }
  .canvas { position: relative; width: 1200px; height: 885px; }

  .card {
    position: absolute; top: 288px;
    width: 540px; height: 309px;
    border-radius: 14px;
    background: linear-gradient(135deg, var(--card-mid) 0%, var(--card-dark) 55%, var(--card-dark) 100%);
    box-shadow: 0 10px 28px rgba(0,0,0,0.25);
    color: var(--ink-light);
    overflow: hidden;
  }
  .card-back { left: 40px; }
  .card-front { left: 620px; }

  .brand-name {
    font-weight: 600;
    letter-spacing: 0.08em;
    text-transform: uppercase;
    color: var(--ink-light);
    line-height: 1;
  }
  .card-back .brand-name {
    position: absolute; left: 0; right: 0; top: 50%;
    transform: translateY(-50%);
    text-align: center; font-size: 50px;
  }
  .card-front .brand-name {
    position: absolute; left: 228px; top: 34px; font-size: 30px;
  }

  .agent-photo {
    position: absolute; left: 52px; top: 92px;
    width: 172px; height: 172px; border-radius: 50%;
    background: radial-gradient(circle at 50% 40%, var(--photo-light) 0%, var(--photo-light) 55%, var(--photo-mid) 100%);
  }

  .agent-name {
    position: absolute; left: 40px; top: 262px;
    font-size: 19px; font-weight: 700; letter-spacing: 0.02em;
    text-transform: uppercase; color: var(--accent-red);
  }
  .agent-title {
    position: absolute; left: 40px; top: 285px;
    font-size: 12px; font-weight: 400; color: var(--ink-light);
  }

  .contact {
    position: absolute; left: 318px; top: 88px;
    font-size: 11.5px; line-height: 1.45; color: var(--ink-soft);
  }
  .contact-address { margin-bottom: 8px; }
  .contact-rule { width: 32px; height: 2px; background: var(--accent-red); margin-bottom: 8px; }
  .contact-list { list-style: none; }
  .contact-item { display: flex; align-items: center; gap: 7px; }
  .contact-icon { width: 11px; height: 11px; flex: none; }
</style>
</head>
<body>
<main class="canvas">

  <section class="card card-back" aria-label="Card back">
    <div class="brand-name">Harborview</div>
  </section>

  <section class="card card-front" aria-label="Card front">
    <div class="brand-name">Harborview</div>

    <div class="agent-photo" role="img" aria-label="Portrait photo of Tomas Villacreces in a dark suit, arms crossed"></div>

    <div class="agent-name">Tomas Villacreces</div>
    <div class="agent-title">Real Estate Professional</div>

    <div class="contact">
      <div class="contact-address">4829 NW 127th St STE 200<br>Palm Hollow, FL 33092</div>
      <div class="contact-rule"></div>
      <ul class="contact-list">
        <li class="contact-item">
          <svg class="contact-icon" viewBox="0 0 12 12"><circle cx="6" cy="6" r="6" fill="var(--accent-red)"/><path d="M3.6 3.2l1.2-.3.7 1.5-.7.5c.4.9 1 1.5 1.9 1.9l.5-.7 1.5.7-.3 1.2C6 8.2 3.8 6 3.6 3.2z" fill="#fff"/></svg>
          305-847-2396
        </li>
        <li class="contact-item">
          <svg class="contact-icon" viewBox="0 0 12 12"><circle cx="6" cy="6" r="6" fill="var(--accent-red)"/><rect x="3" y="4" width="6" height="4.2" fill="none" stroke="#fff" stroke-width=".8"/><path d="M3 4l3 2.3L9 4" fill="none" stroke="#fff" stroke-width=".8"/></svg>
          brightkoda@nestmail.com
        </li>
        <li class="contact-item">
          <svg class="contact-icon" viewBox="0 0 12 12"><circle cx="6" cy="6" r="6" fill="var(--icon-ig)"/></svg>
          @brightkoda
        </li>
        <li class="contact-item">
          <svg class="contact-icon" viewBox="0 0 12 12"><circle cx="6" cy="6" r="6" fill="var(--icon-fb)"/></svg>
          Tomas Villacreces
        </li>
        <li class="contact-item">
          <svg class="contact-icon" viewBox="0 0 12 12"><circle cx="6" cy="6" r="6" fill="var(--icon-in)"/></svg>
          Tomas Villacreces
        </li>
      </ul>
    </div>
  </section>

</main>
</body>
</html>
```